Clinique VeraNova business card

I am looking for a talented designer who can an existing design and make it better. I need a 2 sided business card to represent our Psychology clinic staff members. It would need to be elegant, yet modern, clean, light and uplifting. Simple design, quick turnaround time. Lots of files and logos to use as your guide. I hope to hear from you!

Target Market(s)

Clients who receive the card of our therapists

Industry/Entity Type

Health And Wellness

Contact Information for Business Card

Following the similar designs of the Maplebrook Care Center card, there will be 2 sides. Side 1 (front) should have the veranova logo instead of the maplebrook care logo, The title should read Clinique VeraNova instead of centre Bien-Être Mésange/Maplebrook care Center.

Side 2 should have a spiral similar to the one on the card with sunflower leaves, and the title of the Therapist should be Marielle Odile Brunet, Psychologue, Psychologist, her email: Marielle@Veranova-example.com and phone number should be (514) 555-0137

Font styles to use
Serif

Colors
fee18a
85cae6
ffffff
0255a3

Requirements
Must have
• Side 1 (front): veranova logo- Name of the clinic, clinic address, contact info of clinic etc. use little icons in front of each (just like on sample card)
side 2: Therapist name titles and their contact info underneath with design of spiral and/or sunflower leaves..
Nice to have
• soft colors along soft yellow/gold and blue like the logo,
mini icons for phone, email, address etc.
We do work with a holistic, zen approach so it should represent that to some extent

```html
<!DOCTYPE html>
<html lang="fr">
<head>
<meta charset="utf-8">
<title>Clinique VeraNova – Business Card</title>
<link href="https://fonts.googleapis.com/css2?family=Lato:wght@400;700&display=swap" rel="stylesheet">
<style>
  :root {
    --stage: #fee600;
    --card: #ffffff;
    --navy: #2c2a5e;
    --blue: #2b4d8c;
    --text: #5a5a5a;
    --icon: #85cae6;
    --sun: #fee600;
    --sun-soft: #fee18a;
    --rule: #8a8a8a;
  }
  * { margin: 0; padding: 0; box-sizing: border-box; }
  html, body { width: 833px; height: 1200px; overflow: hidden; }
  body {
    background: var(--stage);
    font-family: "Lato", Arial, sans-serif;
    position: relative;
  }
  .card {
    position: absolute;
    left: 66px;
    width: 700px;
    height: 404px;
    background: var(--card);
  }
  .card--front { top: 166px; }
  .card--back { top: 630px; }

  /* Front */
  .brand {
    position: absolute;
    left: 58px;
    top: 168px;
    display: flex;
    align-items: center;
    gap: 12px;
  }
  .brand__dot {
    width: 44px; height: 44px; border-radius: 50%;
    background: var(--sun);
  }
  .brand__name {
    font-size: 40px;
    font-weight: 700;
    color: var(--navy);
    letter-spacing: 0.5px;
  }
  .divider {
    position: absolute;
    left: 346px; top: 83px;
    width: 1px; height: 242px;
    background: var(--rule);
  }
  .clinic-title {
    position: absolute;
    left: 396px; top: 88px;
    font-size: 21px; font-weight: 700;
    color: var(--blue);
  }
  .contact {
    position: absolute;
    left: 396px;
    font-size: 16.5px;
    line-height: 21px;
    color: var(--text);
    list-style: none;
  }
  .contact li { display: flex; align-items: flex-start; gap: 6px; }
  .contact li .indent { padding-left: 20px; }
  .contact svg { width: 14px; height: 14px; margin-top: 4px; flex: none; }
  .contact--address { top: 150px; }
  .contact--phone { top: 214px; }
  .contact--web { top: 257px; }

  /* Back */
  .spiral-area {
    position: absolute;
    left: 36px; top: 14px;
    width: 320px; height: 376px;
    border-radius: 50%;
    background: radial-gradient(circle at 58% 48%, #fffdf0 0%, var(--sun-soft) 38%, var(--sun) 72%, rgba(254,230,0,0) 73%);
  }
  .person-name {
    position: absolute;
    left: 378px; top: 128px;
    font-size: 21px; font-weight: 700;
    color: var(--blue);
  }
  .person-role {
    position: absolute;
    left: 378px; top: 154px;
    font-size: 17px;
    color: var(--text);
  }
  .contact--person { left: 378px; top: 222px; line-height: 24px; }
</style>
</head>
<body>

<section class="card card--front" aria-label="Card front">
  <div class="brand">
    <span class="brand__dot"></span>
    <span class="brand__name">VeraNova</span>
  </div>
  <div class="divider"></div>
  <h1 class="clinic-title">Clinique VeraNova</h1>

  <ul class="contact contact--address">
    <li>
      <svg viewBox="0 0 14 14"><path d="M7 1a4 4 0 0 0-4 4c0 3 4 8 4 8s4-5 4-8a4 4 0 0 0-4-4zm0 5.5A1.5 1.5 0 1 1 7 3.5a1.5 1.5 0 0 1 0 3z" fill="var(--icon)"/></svg>
      <span>4820 rue des Érables ouest</span>
    </li>
    <li><span class="indent">Lavalière, Qc., H0H 0H0</span></li>
  </ul>

  <ul class="contact contact--phone">
    <li>
      <svg viewBox="0 0 14 14"><path d="M1 8c0-3 3-4 6-4s6 1 6 4l-2 1-1-2H4L3 9z" fill="var(--icon)"/><rect x="4" y="8" width="6" height="3" rx="1" fill="var(--icon)"/></svg>
      <span>514-555-0137</span>
    </li>
  </ul>

  <ul class="contact contact--web">
    <li>
      <svg viewBox="0 0 14 14"><rect x="1" y="3" width="12" height="8" fill="var(--icon)"/><path d="M1 3l6 5 6-5" stroke="#fff" fill="none"/></svg>
      <span>info@veranova.com</span>
    </li>
    <li>
      <svg viewBox="0 0 14 14"><circle cx="7" cy="7" r="5.5" fill="none" stroke="var(--icon)" stroke-width="1.3"/><path d="M1.5 7h11M7 1.5c-3 3-3 8 0 11M7 1.5c3 3 3 8 0 11" fill="none" stroke="var(--icon)"/></svg>
      <span>www.veranova.com</span>
    </li>
    <li>
      <svg viewBox="0 0 14 14"><rect x="1.5" y="1.5" width="11" height="11" fill="var(--icon)"/></svg>
      <span>social.veranova-example.com</span>
    </li>
  </ul>
</section>

<section class="card card--back" aria-label="Card back">
  <div class="spiral-area" role="img" aria-label="Soft yellow brand spiral decoration"></div>
  <h2 class="person-name">Marielle Odile Brunet</h2>
  <p class="person-role">Psychologue, Psychologist</p>
  <ul class="contact contact--person">
    <li>
      <svg viewBox="0 0 14 14"><rect x="4" y="1" width="6" height="12" rx="1.2" fill="none" stroke="var(--icon)" stroke-width="1.3"/><circle cx="7" cy="11" r="0.8" fill="var(--icon)"/></svg>
      <span>(514) 555-0137</span>
    </li>
    <li>
      <svg viewBox="0 0 14 14"><rect x="1" y="3" width="12" height="8" fill="var(--icon)"/><path d="M1 3l6 5 6-5" stroke="#fff" fill="none"/></svg>
      <span>mailto:marielle@veranova-example.com</span>
    </li>
  </ul>
</section>

</body>
</html>
```